Letterhead Design for Law Firm

**Edit: I have added the photo of a bottom that I like.

------
We are looking for a re-design of our new letterhead. The letterhead is for a law firm and will be used for digital and traditionally printed correspondence.

Here are some suggestions:

- Please use colours are #8ec900 and simple black.
- Please do not use any type of "waves" at the bottom of the page. This is not in style at all.
- Please stay modern yet conservative.
- Please use font Segoe UI Light or similar if you can
- Avoid clipart or illustrations.
- Utilize ample white space in the layout so the design looks clean and information is easy to read at a glance. Don't overcrowd the letterhead.
- Make sure the letterhead design is consistent with our brand identity (see harbolt.ca)
-Please, no black headers or footers.

I am attaching my current letterhead and signature for your convenience.

Remember, the letterhead is an extension of our professional identity. We are a successful firm and trial lawyers who correspond with insurers, judges, lawyers, courts, clients, etc. Make it new, modern, attractive, yet powerful and conservative.

It needs to be easily printable. I would like the bleed removed in print so the black bar the bottom crosses the page (but the text is not near the edges)

Target Market(s)

Clients, Government Offices, Judiciary, Lawyers, Insurance Companies, Colleagues.

Industry/Entity Type

Law

Font styles to use
Other font styles liked:
• Segoe UI LIght, Calibri Light,

Colors
00AB8E
00BBA5
67D7C9
C6EFE9
E9F9F6

Requirements
Must have
• Everything that is on the letterhead now.
Nice to have
• Cutting Edge design, yet conservative.
Should not have
• law firm cliche design, images,

```html
<!DOCTYPE html>
<html lang="en">
<head>
<meta charset="utf-8">
<title>Harbolt Personal Injury Lawyers – Letterhead</title>
<link href="https://fonts.googleapis.com/css2?family=Roboto:wght@300;400;500;700&family=Arimo:wght@400&display=swap" rel="stylesheet">
<style>
  :root{
    --paper:#f6f4f4;
    --ink:#1c1c1c;
    --muted:#555555;
    --green:#9bcc55;
    --bar:#1d1d1d;
  }
  *{box-sizing:border-box;margin:0;padding:0}
  html,body{width:935px;height:1200px;overflow:hidden;background:var(--paper)}
  body{font-family:"Roboto",sans-serif;color:var(--ink);position:relative}
  .abs{position:absolute}
  .brand{left:44px;top:64px}
  .brand-name{font-family:"Roboto",sans-serif;font-weight:500;font-size:64px;letter-spacing:1px;line-height:1;color:var(--ink)}
  .brand-tag{font-weight:400;font-size:15px;letter-spacing:1.6px;margin-top:6px;color:var(--ink)}
  .contact{left:636px;top:52px;font-size:14px;line-height:19px;color:var(--ink)}
  .contact-lines{margin-top:8px}
  .contact-lines div{display:flex;align-items:center;gap:6px}
  .contact svg{width:13px;height:13px;flex:none}
  .clerk{left:636px;top:167px;font-size:16px}
  .clerk b{font-weight:500}
  .clerk span{color:var(--muted)}
  .label{font-weight:500;font-size:15px}
  .prejudice{left:44px;top:205px}
  .delivery{left:44px;top:253px}
  .date{right:55px;top:253px;font-size:15px}
  .recipient{left:44px;top:292px;font-size:16px;line-height:20px}
  .attention{left:44px;top:417px;font-size:16px}
  .salutation{left:44px;top:444px;font-size:16px}
  .re-label{left:44px;top:483px}
  .re-text{left:327px;top:481px;font-size:16px;line-height:20px}
  .rule{left:56px;top:564px;width:815px;height:1px;background:#333}
  .body{left:54px;top:590px;width:831px;font-family:"Arimo",sans-serif;font-size:13.4px;line-height:20.4px;color:#3a3a3a}
  .body p{margin-bottom:20px}
  .closing{left:56px;top:890px;font-size:14px;line-height:17.5px}
  .signature{left:56px;top:936px;width:260px;height:58px}
  .signer{left:60px;top:1013px;font-size:14px;line-height:17.7px}
  .practice{right:40px;top:1078px;text-align:right;font-size:14.5px;line-height:19.5px;color:var(--muted)}
  .practice b{font-weight:500;color:#333}
  .bar-dark{left:0;top:1176px;width:601px;height:24px;background:var(--bar)}
  .bar-green{left:606px;top:1176px;width:329px;height:24px;background:var(--green);font-weight:700;font-size:14.5px;line-height:24px;padding-left:100px;color:var(--ink)}
</style>
</head>
<body>
  <header>
    <div class="abs brand">
      <div class="brand-name">HARBOLT</div>
      <div class="brand-tag">PERSONAL INJURY LAWYERS</div>
    </div>
    <div class="abs contact">
      <div>48 Garnet Street W., Suite 1210</div>
      <div>Hamilton, ON&nbsp; L8P 2B6</div>
      <div class="contact-lines">
        <div><svg viewBox="0 0 16 16"><path fill="var(--green)" d="M3.5 1l2.5 3-1.5 2c1 2 3 4 5 5l2-1.5 3 2.5-1.5 2.5C8 15 1 8 1 2.5z"/></svg>905-555-0142</div>
        <div><svg viewBox="0 0 16 16"><rect x="4" y="1" width="8" height="5" fill="var(--green)"/><rect x="1" y="6" width="14" height="7" rx="1" fill="var(--green)"/><rect x="4" y="10" width="8" height="5" fill="#fff" stroke="var(--green)"/></svg>905-555-0187</div>
        <div><svg viewBox="0 0 16 16"><rect x="1" y="3" width="14" height="10" fill="var(--green)"/><path d="M1 3l7 6 7-6" fill="none" stroke="#fff" stroke-width="1.4"/></svg>Email: joanna@harbolt.ca</div>
      </div>
    </div>
    <div class="abs clerk"><b>File Clerk:</b> <span>Joanna Whitfield</span></div>
  </header>

  <main>
    <div class="abs label prejudice">Without Prejudice</div>
    <div class="abs label delivery">By Email</div>
    <div class="abs date">March 13, 2024</div>
    <address class="abs recipient" style="font-style:normal">
      Northvale Insurance Company<br>
      Claims Litigation Department<br>
      275 Larchmont Road South<br>
      P.O. Box 4100<br>
      Waterloo, ON&nbsp;&nbsp; N2J 3K7
    </address>
    <div class="abs attention">Attention:&nbsp; Mr. Colin Marsh</div>
    <div class="abs salutation">Mr. Marsh:</div>
    <div class="abs label re-label">Re:</div>
    <div class="abs re-text">
      Varga v. Pemberton et al.<br>
      DOL:&nbsp; September 12, 2019<br>
      Pre-Mediation Settlement Proposal – March 13th, 2024
    </div>
    <div class="abs rule"></div>

    <div class="abs body">
      <p>Lorem ipsum dolor sit amet, consectetur adipiscing elit. Donec orci purus, luctus vitae dignissim eu, iaculis sed purus. Vivamus faucibus, ipsum nec aliquet viverra, leo mauris condimentum ligula, sit amet sagittis enim ligula quis arcu. Nam egestas tortor ivisi porttitor mattis. In tortor ante, ultricies in suscipit a, tempus non massa. Vivamus et auctor mi. Fusce vel massa nulla. Phasellus nec eros mauris, et scelerisque orci.</p>
      <p>Donec malesuada orci vitae nulla accumsan porta a id massa. Quisque accumsan iaculis magna sit amet fringilla. Maecenas consequat, magna eget tincidunt semper, odio nibh rutrum mi, id feugiat ante nisi eu risus. Vestibulum nunc orci, rhoncus a placerat in, ultricies in mi. Cras mattis varius eros, vel fringilla nisi suscipit eget. Quisque scelerisque sagittis nulla at porttitor.</p>
      <p>Sed id augue vitae urna euismod commodo aliquet a quam. Pellentesque arcu velit, cursus et malesuada ut, consequat et diam. Nullam erat sem, rhoncus id ullamcorper vitae, rhoncus et arcu. In ultricies ultricies nulla, ut rutrum nisi iaculis</p>
    </div>

    <div class="abs closing">Yours very truly,<br>HARBOLT PERSONAL INJURY LAWYERS</div>
    <svg class="abs signature" role="img" aria-label="Handwritten signature of Daniel K. Harbolt" viewBox="0 0 260 58">
      <defs><linearGradient id="sigTone" x1="0" x2="1"><stop offset="0" stop-color="#dddbdb"/><stop offset="1" stop-color="#eceaea"/></linearGradient></defs>
      <rect width="260" height="58" fill="url(#sigTone)"/>
    </svg>
    <div class="abs signer">Daniel K. Harbolt<br>Harbolt Law Professional Corporation<br>/jw<br>Encl.</div>
  </main>

  <footer>
    <div class="abs practice"><b>Practice Restricted-</b> Serious Personal Injury, Wrongful Death Litigation<br>Long-Term Disability Litigation, Wrongful Dismissal Litigation<br>Employee Terminations</div>
    <div class="abs bar-dark"></div>
    <div class="abs bar-green">www.HARBOLT.ca</div>
  </footer>
</body>
</html>
```